Velvet Glow Co. Derma Roller packaging design

I need a box designed for a skin care brand called Velvet Glow Co. The box will be for our Derma Roller- a skin rejuvenation device. It will be sold online with lots of competition. I would like a modern, high end design, something that stands out and looks amazing. My logo is blush pink and black, for packaging i need no more than 3 colours, maybe gold if any other colour is used. A photo of a sample derma roller is attached below for an idea of what the product looks like, however my roller with have a clear handle with a black roller. The roller comes in a clear case, the box dimensions will need to be 16 cm long, 4 cm high, 4.5 cm wide.
ATTACHED ARE 2 SAMPLE BOXES AS AN EXAMPLE OF THE SIZE OF BOX REQUIRED!

Target Market(s)

25-50 year old women in the US

Colors
e667a6
000000
efefef

Requirements
Must have
• LOGO
• NAME OF PRODUCT- Cosmetic Derma Roller
• NEEDLE DEPTH- 0.25mm
• CAUTION- For personal use only, Do not use if allergic to metal, Do not use on open skin, wounds or active acne, sterilise roller before and after use.
Nice to have
• BENEFITS- Skin Rejuvenation, Collagen Induction Therapy, Increase product absorption, reduce acne scars and pigmentation
• FEATURES- 540 high quality titanium needles, ultra sharp needle tips, cross-line needle arrangement, ergonomic handle, anti slip grip,

```html
<!DOCTYPE html>
<html lang="en">
<head>
<meta charset="utf-8">
<title>Velvet Glow Co. – Cosmetic Derma Roller Packaging</title>
<link href="https://fonts.googleapis.com/css2?family=Oswald:wght@400;500&display=swap" rel="stylesheet">
<style>
  :root {
    --page-bg: #fbf8f7;
    --marble-light: #f7f5f2;
    --marble-mid: #e6e4e2;
    --marble-vein: #b9b8b8;
    --ink: #1c1c1c;
    --rose-gold-light: #f2c8b6;
    --rose-gold-dark: #c98e7a;
    --panel-shadow: rgba(60, 50, 50, 0.35);
  }
  * { margin: 0; padding: 0; box-sizing: border-box; }
  html, body {
    width: 1200px;
    height: 1200px;
    overflow: hidden;
    background: radial-gradient(ellipse at center, #ffffff 0%, var(--page-bg) 70%, #f6efed 100%);
    font-family: "Oswald", "Arial Narrow", sans-serif;
  }
  .canvas { position: relative; width: 1200px; height: 1200px; }

  .box-panel {
    position: absolute;
    left: 48px;
    width: 1104px;
    height: 356px;
    box-shadow: 0 3px 8px var(--panel-shadow);
    overflow: hidden;
  }
  .box-panel--front { top: 182px; }
  .box-panel--back { top: 662px; }

  .marble-surface {
    position: absolute;
    inset: 0;
    background:
      radial-gradient(ellipse 30% 45% at 12% 70%, var(--marble-mid), transparent 70%),
      radial-gradient(ellipse 25% 40% at 85% 30%, var(--marble-mid), transparent 70%),
      radial-gradient(ellipse 35% 30% at 50% 95%, #dcdad8, transparent 70%),
      linear-gradient(160deg, var(--marble-light) 0%, #eeecea 45%, var(--marble-light) 100%);
  }

  .brand-name {
    position: absolute;
    top: 148px;
    left: 0;
    right: 0;
    display: flex;
    justify-content: center;
    align-items: center;
    gap: 14px;
    font-weight: 400;
    font-size: 34px;
    letter-spacing: 4px;
    color: var(--ink);
    text-transform: uppercase;
  }
  .brand-mark {
    width: 16px;
    height: 16px;
    border: 1px solid var(--ink);
  }

  .product-title {
    position: absolute;
    left: 0;
    right: 0;
    text-align: center;
    font-weight: 500;
    font-size: 29px;
    letter-spacing: 0.5px;
    background: linear-gradient(90deg, var(--rose-gold-light), var(--rose-gold-dark) 50%, var(--rose-gold-light) 75%, var(--rose-gold-dark));
    -webkit-background-clip: text;
    background-clip: text;
    color: transparent;
  }
  .box-panel--front .product-title { top: 256px; }
  .box-panel--back .product-title { top: 56px; }

  .product-details {
    position: absolute;
    left: 277px;
    top: 124px;
    width: 580px;
    font-size: 14.5px;
    line-height: 22px;
    color: var(--ink);
    text-transform: uppercase;
  }
  .product-details p + p { margin-top: 24px; }
</style>
</head>
<body>
<main class="canvas">
  <section class="box-panel box-panel--front">
    <div class="marble-surface" role="img" aria-label="White marble texture with grey veins"></div>
    <div class="brand-name"><span class="brand-mark"></span>Velvet Glow Co.</div>
    <h1 class="product-title">Cosmetic Derma Roller</h1>
  </section>

  <section class="box-panel box-panel--back">
    <div class="marble-surface" role="img" aria-label="White marble texture with grey veins"></div>
    <h2 class="product-title">Cosmetic Derma Roller</h2>
    <div class="product-details">
      <p>Benefits: skin rejuvenation, collagen induction therapy, increase product absorption, reduce acne scars and pigmentation</p>
      <p>Features: 540 high quality 0.25 mm titanium needles, ultra sharp needle tips, cross-line needle arrangement, ergonomic handle, anti slip grip</p>
      <p>Caution: for personal use only, do not use if allergic to metal, do not use on open skin, wounds or active acne, sterilise roller before and after use.</p>
    </div>
  </section>
</main>
</body>
</html>
```